M Zyvantics Buisness Cards

I need a technology focused clean business card for my employees. I have attached out logo to include in the mocks. We're a modern tech consulting firm that drives to interface humanity with technology in a truly cohesive fashion.

```html
<!DOCTYPE html>
<html lang="en">
<head>
<meta charset="UTF-8">
<title>M Zyvantics Employee ID Card</title>
<link rel="stylesheet" href="https://fonts.googleapis.com/css2?family=Montserrat:wght@500;600;700;800&display=swap">
<style>
  :root {
    --card-light: #f4f4f4;
    --card-mid: #d6d6d6;
    --card-dark: #bdbdbd;
    --brand-grey: #55585b;
    --brand-blue: #3d6db4;
    --ink-dark: #1d1d1d;
    --photo-fill: #121212;
    --text-light: #ffffff;
  }
  * { margin: 0; padding: 0; box-sizing: border-box; }
  html, body {
    width: 758px;
    height: 1200px;
    overflow: hidden;
    background: #ffffff;
  }
  .id-card {
    position: relative;
    width: 758px;
    height: 1200px;
    overflow: hidden;
    font-family: "Montserrat", sans-serif;
    background:
      linear-gradient(160deg, rgba(255,255,255,0.55) 0%, rgba(255,255,255,0) 45%),
      linear-gradient(200deg, var(--card-light) 0%, var(--card-mid) 45%, var(--card-light) 70%, var(--card-dark) 100%);
  }
  .brand {
    position: absolute;
    top: 92px;
    left: 0;
    width: 100%;
    display: flex;
    flex-direction: column;
    align-items: center;
  }
  .brand-lockup {
    display: flex;
    align-items: center;
    gap: 22px;
  }
  .brand-dot {
    width: 74px;
    height: 74px;
    border-radius: 50%;
    background: var(--brand-blue);
  }
  .brand-name {
    font-size: 76px;
    font-weight: 700;
    color: var(--brand-grey);
    letter-spacing: 1px;
    line-height: 1;
  }
  .brand-tagline {
    margin-top: 26px;
    margin-left: 96px;
    font-size: 14px;
    font-weight: 600;
    letter-spacing: 5px;
    color: var(--ink-dark);
  }
  .photo-slot {
    position: absolute;
    left: 207px;
    top: 376px;
    width: 344px;
    height: 344px;
    border-radius: 50%;
    background: var(--photo-fill);
    display: flex;
    align-items: center;
    justify-content: center;
    text-align: center;
  }
  .photo-slot span {
    color: var(--text-light);
    font-size: 25px;
    font-weight: 700;
    line-height: 1.45;
  }
  .employee {
    position: absolute;
    top: 806px;
    left: 0;
    width: 100%;
    text-align: center;
    color: var(--text-light);
  }
  .employee-name {
    font-size: 42px;
    font-weight: 700;
    line-height: 1.1;
  }
  .employee-role {
    margin-top: 10px;
    font-size: 19px;
    font-weight: 700;
  }
  .employee-id {
    margin-top: 14px;
    font-size: 11px;
    font-weight: 700;
    letter-spacing: 3.5px;
    color: var(--ink-dark);
  }
  .contact-line {
    position: absolute;
    bottom: 26px;
    left: 0;
    width: 100%;
    text-align: center;
    font-size: 20px;
    font-weight: 600;
    letter-spacing: 6.5px;
    color: var(--ink-dark);
  }
</style>
</head>
<body>
  <main class="id-card">
    <header class="brand">
      <div class="brand-lockup">
        <div class="brand-dot" aria-hidden="true"></div>
        <div class="brand-name">M Zyvantics</div>
      </div>
      <div class="brand-tagline">YOUR BUSINESS TAGLINE HERE</div>
    </header>

    <div class="photo-slot" role="img" aria-label="Employee portrait photo area">
      <span>EMPLOYEE IMAGE<br>HERE</span>
    </div>

    <section class="employee">
      <h1 class="employee-name">EMPLOYEE NAME</h1>
      <p class="employee-role">EMPLOYEE DESIGNATION</p>
      <p class="employee-id">EMPLOYEE ID NUMBER</p>
    </section>

    <footer class="contact-line">YOUR BUSINESS CONTACT DETAILS HERE</footer>
  </main>
</body>
</html>
```